Bright Oak Consultant Services

I'm looking to create a flyer for my business to provide a consultant service. I will be providing the following below
Launch Your Business Today for only $150
(state fee not included)
Business Formation includes:
*Limited liability Corporation (LLC)
*Hale and Penwick Number
*FEIN
*Operation Agreement for partnership LLCs (For 2 or more member(s)
*Commercial Activity license (If needed for your Business )
*Same -day turnaround service with documents
Schedule your Appointment today
Call or text:413-902-6175
Email:MorvellCapitalCircle@quillpost.net
Target Market(s)
I want the flyer to attract people who wants to start a business but doesn’t know where to start. I want the flyer to stand out form the other consultant businesses.
Industry/Entity Type
Consultant
Requirements
Must have
- The State fee not included should be in small print
Highlight the price or service
Highlight the phrase "launch you business today"
Nice to have
- Different samples of colors, a variety
Should not have
- should not be all one color

```html
<!DOCTYPE html>
<html lang="en">
<head>
<meta charset="utf-8">
<title>Morvell Capital Circle – Launch Your Business Today</title>
<link rel="stylesheet" href="https://fonts.googleapis.com/css2?family=Jost:wght@300;400;500;600;700&family=Montserrat:wght@800&display=swap">
<style>
  :root {
    --ink: #20232b;
    --sky: #9cc3e6;
    --brand-blue: #8db0dc;
    --teal-dot: #1aa583;
    --orange: #f58d4b;
    --red: #ee4a50;
    --gold: #fbb034;
    --panel: rgba(186, 86, 168, 0.82);
    --price-box: rgba(60, 178, 180, 0.82);
    --cta-green: #3aa883;
    --cta-frame: #c26a3a;
    --phone: #7193d4;
    --white: #ffffff;
  }
  * { margin: 0; padding: 0; box-sizing: border-box; }
  html, body { width: 888px; height: 1200px; overflow: hidden; background: var(--ink); }
  .flyer {
    position: relative; width: 888px; height: 1200px; overflow: hidden;
    background: var(--ink); font-family: "Jost", sans-serif; color: var(--white);
  }

  /* Header */
  .brand-mark {
    position: absolute; left: 74px; top: 53px; width: 184px; height: 142px;
    background: var(--sky);
  }
  .brand-name {
    position: absolute; left: 272px; top: 78px;
    color: var(--brand-blue); font-weight: 600; line-height: 1;
  }
  .brand-name .line-main { display: block; font-size: 46px; letter-spacing: 1px; }
  .brand-name .line-sub { display: block; font-size: 15px; letter-spacing: 6.5px; margin-top: 8px; }
  .social { position: absolute; top: 164px; left: 666px; display: flex; gap: 6px; }
  .social span { width: 31px; height: 31px; border-radius: 50%; background: var(--teal-dot); }

  /* Hero */
  .hero-photo {
    position: absolute; left: 0; top: 241px; width: 888px; height: 737px;
    background:
      radial-gradient(ellipse at 85% 10%, rgba(70, 170, 230, 0.9), transparent 55%),
      radial-gradient(ellipse at 20% 40%, rgba(40, 130, 215, 0.8), transparent 60%),
      linear-gradient(180deg, #2a74c8 0%, #2a62b8 55%, #27489a 85%, #2c3f78 100%);
  }
  .headline { position: absolute; left: 0; top: 0; width: 888px; height: 1200px; }
  .headline text { font-family: "Jost", sans-serif; }

  /* Price box */
  .price-box {
    position: absolute; left: 72px; top: 625px; width: 342px; height: 273px;
    background: var(--price-box); border-top-left-radius: 40px; text-align: center;
  }
  .price-lead { position: absolute; top: 30px; left: 0; right: 0; font-size: 24px; font-weight: 600; letter-spacing: 6px; }
  .price-amount { position: absolute; left: 20px; top: 58px; font-weight: 600; line-height: 1; }
  .price-amount .currency { position: absolute; left: 0; top: 10px; font-size: 52px; font-weight: 500; }
  .price-amount .figure { display: block; margin-left: 36px; font-size: 168px; letter-spacing: -8px; }
  .fine-print { position: absolute; top: 216px; left: 0; right: 0; font-size: 21px; font-weight: 400; }

  /* Inclusions panel */
  .includes {
    position: absolute; left: 446px; top: 513px; width: 365px; height: 638px;
    background: var(--panel); border-bottom-right-radius: 42px;
  }
  .includes h2 {
    position: absolute; left: 31px; top: 45px; color: var(--gold);
    font-size: 49px; font-weight: 700; line-height: 52px; letter-spacing: 0.3px;
  }
  .includes .rule { position: absolute; left: 31px; top: 225px; width: 299px; height: 2px; background: var(--gold); }
  .includes ul { position: absolute; left: 37px; top: 260px; width: 320px; list-style: none; }
  .includes li { position: relative; padding-left: 16px; font-size: 20px; font-weight: 400; line-height: 23px; margin-bottom: 17px; }
  .includes li::before { content: ""; position: absolute; left: 0; top: 8px; width: 7px; height: 7px; border-radius: 50%; background: var(--white); }

  /* Footer */
  .cta {
    position: absolute; left: 72px; top: 1042px; width: 327px; height: 61px;
    border: 1px solid var(--cta-frame); border-top-right-radius: 18px;
    padding: 10px 0 0 15px;
    font-family: "Montserrat", sans-serif; font-weight: 800; font-size: 19px;
    line-height: 22px; letter-spacing: 2px; color: var(--cta-green);
  }
  .contact { position: absolute; left: 87px; top: 1110px; font-size: 14px; line-height: 18px; }
  .contact .phone { font-size: 21px; font-weight: 600; color: var(--phone); letter-spacing: 0.5px; }
</style>
</head>
<body>
<main class="flyer">
  <header>
    <div class="brand-mark"></div>
    <div class="brand-name"><span class="line-main">MORVELL</span><span class="line-sub">CAPITAL CIRCLE</span></div>
    <div class="social"><span></span><span></span><span></span><span></span></div>
  </header>

  <div class="hero-photo" role="img" aria-label="Blue-tinted photo of business paperwork and a rising arrow chart"></div>

  <svg class="headline" viewBox="0 0 888 1200" aria-label="Launch Your Business Today">
    <text x="71" y="368" font-size="74" font-weight="500" fill="#ffffff" textLength="424" lengthAdjust="spacingAndGlyphs">Launch Your</text>
    <text x="69" y="490" font-size="132" font-weight="700" fill="#f58d4b" textLength="670" lengthAdjust="spacingAndGlyphs">BUSINESS</text>
    <text x="69" y="583" font-size="118" font-weight="700" fill="#ee4a50" textLength="360" lengthAdjust="spacingAndGlyphs">TODAY</text>
  </svg>

  <section class="price-box">
    <p class="price-lead">FOR ONLY</p>
    <p class="price-amount"><span class="currency">$</span><span class="figure">150</span></p>
    <p class="fine-print">(state fee not included)</p>
  </section>

  <section class="includes">
    <h2>BUSINESS<br>FORMATION<br>INCLUDES:</h2>
    <div class="rule"></div>
    <ul>
      <li>Limited Liability Corporation (LLC)</li>
      <li>Hale and Penwick Number</li>
      <li>FEIN</li>
      <li>Operation Agreement for partnership LLCs<br>(For 2 or more member(s)</li>
      <li>Commercial Activity license<br>(If needed for your Business )</li>
      <li>Same-day turnaround service with documents</li>
    </ul>
  </section>

  <footer>
    <div class="cta">SCHEDULE YOUR<br>APPOINTMENT TODAY</div>
    <div class="contact">
      <p>Call or Text: <span class="phone">413-902-6175</span></p>
      <p>Email: MorvellCapitalCircle@quillpost.net</p>
    </div>
  </footer>
</main>
</body>
</html>
```